Unique and original Business Card for Financial Services Business

I have moved premises and need to change the detail on my business card so thought now is a good time for a re-design. Looking for something professional and modern with colours to fit in with out logo. Like the idea of foil or embossing if that works but not a must have but I do want something that stands out and that I could not design myself.

Once business card is designed I will also be looking to get letterhead and flyers done but want the business card concept in place first.

The majority of designs I am receiving are generic and template based. I am looking for something unique and original. We have some great design elements in our logo, think outside the box and show me something that stands out from the crowd.

Target Market(s)

Business Professionals

Industry/Entity Type

Finance

Contact Information for Business Card

Name: Delphine Moore Phone 0438 297 614 Address PO Box 7816 Ashvale NSW 2411 Email info@tidewellmoneyservices.example.com.au website www.tidewellmoneyservices.example.com.au

Font styles to use
Other font styles liked:
• Ralway

Requirements
Should not have
• No black backgrounds please

```html
<!DOCTYPE html>
<html lang="en">
<head>
<meta charset="utf-8">
<title>Tidewell Money Services – Business Card</title>
<link rel="stylesheet" href="https://fonts.googleapis.com/css2?family=Open+Sans:wght@400;600;700&family=Raleway:wght@300;400;600&display=swap">
<style>
  :root {
    --stage: #3b3b3b;
    --card: #263840;
    --card-back: #22333a;
    --teal: #3ea3b3;
    --teal-light: #63c3d1;
    --ink: #eef3f4;
    --muted: #b8c9ce;
    --emboss: #314650;
  }
  * { box-sizing: border-box; margin: 0; padding: 0; }
  html, body {
    width: 1200px; height: 801px; overflow: hidden;
    background: var(--stage);
  }
  .stage {
    width: 1200px; height: 801px;
    display: flex; align-items: center; justify-content: center; gap: 40px;
  }
  .card {
    position: relative;
    width: 520px; height: 297px;
    background: var(--card);
    box-shadow: 0 0 0 1px var(--teal), 0 14px 30px rgba(0,0,0,.4);
  }
  /* front */
  .brand {
    position: absolute; left: 34px; top: 52px;
    display: flex; align-items: center; gap: 12px;
  }
  .brand__dot {
    width: 34px; height: 34px; border-radius: 50%;
    background: var(--teal);
  }
  .brand__name {
    font-family: 'Raleway', sans-serif; font-weight: 300;
    font-size: 30px; line-height: 1; letter-spacing: .5px;
    color: var(--teal-light); text-transform: uppercase;
  }
  .brand__tag {
    display: block; margin-top: 6px;
    font-family: 'Raleway', sans-serif; font-weight: 300;
    font-size: 12px; letter-spacing: 6px; color: var(--teal-light);
  }
  .person {
    position: absolute; right: 32px; top: 44px; text-align: right;
  }
  .person__name {
    font-family: 'Open Sans', sans-serif; font-weight: 700;
    font-size: 21px; color: var(--teal-light); text-transform: uppercase;
    letter-spacing: -.3px;
  }
  .person__role {
    font-family: 'Open Sans', sans-serif; font-size: 14px; color: var(--ink);
  }
  .divider {
    position: absolute; left: 34px; right: 32px; top: 168px;
    height: 1px; background: var(--teal);
  }
  .contacts {
    position: absolute; left: 34px; top: 188px;
    list-style: none;
    font-family: 'Open Sans', sans-serif; font-size: 12.5px; color: var(--ink);
  }
  .contacts li { display: flex; align-items: center; gap: 8px; line-height: 24px; }
  .contacts svg { width: 12px; height: 12px; fill: var(--muted); flex: none; }
  .address {
    position: absolute; right: 32px; top: 188px; text-align: right;
    font-family: 'Open Sans', sans-serif; font-size: 13px; line-height: 22px;
    color: var(--ink); font-style: normal;
  }
  /* back */
  .card--back { background: var(--card-back); display: flex; align-items: center; justify-content: center; }
  .back-mark {
    font-family: 'Raleway', sans-serif; font-weight: 600;
    font-size: 44px; color: var(--emboss); text-transform: uppercase;
    letter-spacing: 2px;
  }
</style>
</head>
<body>
<main class="stage">
  <section class="card card--front" aria-label="Business card front">
    <div class="brand">
      <span class="brand__dot" aria-hidden="true"></span>
      <div class="brand__name">Tidewell
        <span class="brand__tag">Money Services</span>
      </div>
    </div>

    <div class="person">
      <p class="person__name">Delphine Moore</p>
      <p class="person__role">President</p>
    </div>

    <div class="divider"></div>

    <ul class="contacts">
      <li>
        <svg viewBox="0 0 24 24" aria-hidden="true"><path d="M6.6 10.8a15.1 15.1 0 0 0 6.6 6.6l2.2-2.2c.3-.3.7-.4 1-.2 1.1.4 2.3.6 3.6.6.6 0 1 .4 1 1V20c0 .6-.4 1-1 1A17 17 0 0 1 3 4c0-.6.4-1 1-1h3.5c.6 0 1 .4 1 1 0 1.3.2 2.5.6 3.6.1.3 0 .7-.2 1z"/></svg>
        0438 297 614
      </li>
      <li>
        <svg viewBox="0 0 24 24" aria-hidden="true"><path d="M2 5h20v14H2zm2 2v.5l8 5 8-5V7l-8 5z"/></svg>
        info@tidewellmoneyservices.example.com.au
      </li>
      <li>
        <svg viewBox="0 0 24 24" aria-hidden="true"><path d="M12 2a10 10 0 1 0 0 20 10 10 0 0 0 0-20zm0 2c1 0 2.3 2 2.8 5H9.2C9.7 6 11 4 12 4zM4.3 11h4.7c0 .7 0 1.4.1 2H4.3a8 8 0 0 1 0-2zm.6 4h4.4c.3 1.8.9 3.3 1.6 4.3A8 8 0 0 1 4.9 15zm10 0h4.2a8 8 0 0 1-5.9 4.3c.8-1 1.4-2.5 1.7-4.3zm.2-4h4.6a8 8 0 0 1 0 2h-4.6c.1-.6.1-1.3 0-2z"/></svg>
        www.tidewellmoneyservices.example.com.au
      </li>
    </ul>

    <address class="address">
      PO Box 7816<br>
      Ashvale NSW 2411
    </address>
  </section>

  <section class="card card--back" aria-label="Business card back">
    <span class="back-mark">Tidewell</span>
  </section>
</main>
</body>
</html>
```